Book cover for LS

Design cover for a book of gratitude and inspiration.
Book trim size will be 6.5 x 6.5 inches, or 8 x 8 inches, hardcover, 96 pages
Title: Lantern Stones
Subtitle: A Book of Gratitude and Inspiration
Author: Carl Wendover

```html
<!DOCTYPE html>
<html lang="en">
<head>
<meta charset="utf-8">
<title>Lantern Stones – Book Cover</title>
<link href="https://fonts.googleapis.com/css2?family=Amatic+SC:wght@700&family=Oswald:wght@400;500&display=swap" rel="stylesheet">
<style>
  :root {
    --stage: #808080;
    --paper: #f1f0f0;
    --blush: #efc6c8;
    --mist: #d3dce3;
    --sand: #efe1d4;
    --slate: #3c5568;
    --leaf: #a8c9a0;
    --gold: #d6b25c;
    --ink: #324a5e;
    --sky: #6b95c6;
    --white: #ffffff;
    --author: #0d0d14;
  }
  * { margin: 0; padding: 0; box-sizing: border-box; }
  html, body {
    width: 1195px;
    height: 1200px;
    overflow: hidden;
    background: var(--stage);
  }
  .cover {
    position: absolute;
    left: 130px;
    top: 118px;
    width: 935px;
    height: 935px;
    overflow: hidden;
    background: var(--paper);
  }
  .cover__artwork {
    position: absolute;
    inset: 0;
    width: 100%;
    height: 100%;
  }
  .cover__title {
    position: absolute;
    left: 256px;
    top: 214px;
    font-family: "Amatic SC", cursive;
    font-weight: 700;
    font-size: 174px;
    line-height: 0.75;
    color: var(--ink);
    letter-spacing: 3px;
    -webkit-text-stroke: 14px var(--white);
    paint-order: stroke fill;
  }
  .cover__title span { display: block; }
  .cover__subtitle {
    position: absolute;
    left: 256px;
    top: 494px;
    height: 38px;
    padding: 0 6px;
    background: var(--white);
    font-family: "Oswald", sans-serif;
    font-weight: 500;
    font-size: 29px;
    line-height: 38px;
    color: var(--sky);
    text-transform: uppercase;
    letter-spacing: -0.3px;
    white-space: nowrap;
  }
  .cover__author {
    position: absolute;
    left: 0;
    right: 0;
    top: 822px;
    text-align: center;
    padding-left: 60px;
    font-family: "Oswald", sans-serif;
    font-weight: 500;
    font-size: 31px;
    color: var(--author);
  }
</style>
</head>
<body>
  <main class="cover">
    <svg class="cover__artwork" viewBox="0 0 935 935" role="img" aria-label="Soft floral illustration: translucent snowdrops, slate leaves, a golden sprig and abstract blush and grey-blue petals" preserveAspectRatio="none">
      <defs>
        <radialGradient id="wash-mist-top"><stop offset="0" stop-color="var(--mist)"/><stop offset="1" stop-color="var(--mist)" stop-opacity="0"/></radialGradient>
        <radialGradient id="wash-blush"><stop offset="0" stop-color="var(--blush)"/><stop offset="1" stop-color="var(--blush)" stop-opacity="0"/></radialGradient>
        <radialGradient id="wash-sand"><stop offset="0" stop-color="var(--sand)"/><stop offset="1" stop-color="var(--sand)" stop-opacity="0"/></radialGradient>
        <radialGradient id="wash-slate"><stop offset="0" stop-color="var(--slate)" stop-opacity="0.55"/><stop offset="1" stop-color="var(--slate)" stop-opacity="0"/></radialGradient>
        <radialGradient id="wash-leaf"><stop offset="0" stop-color="var(--leaf)" stop-opacity="0.6"/><stop offset="1" stop-color="var(--leaf)" stop-opacity="0"/></radialGradient>
        <radialGradient id="wash-gold"><stop offset="0" stop-color="var(--gold)" stop-opacity="0.5"/><stop offset="1" stop-color="var(--gold)" stop-opacity="0"/></radialGradient>
        <radialGradient id="wash-white"><stop offset="0" stop-color="var(--white)"/><stop offset="1" stop-color="var(--white)" stop-opacity="0"/></radialGradient>
      </defs>
      <rect width="935" height="935" fill="var(--paper)"/>
      <ellipse cx="200" cy="90" rx="240" ry="170" fill="url(#wash-mist-top)"/>
      <ellipse cx="640" cy="90" rx="320" ry="200" fill="url(#wash-blush)"/>
      <ellipse cx="60" cy="300" rx="200" ry="230" fill="url(#wash-blush)"/>
      <ellipse cx="900" cy="330" rx="160" ry="240" fill="url(#wash-blush)"/>
      <ellipse cx="640" cy="420" rx="330" ry="160" fill="url(#wash-mist-top)"/>
      <ellipse cx="450" cy="500" rx="420" ry="160" fill="url(#wash-sand)"/>
      <ellipse cx="600" cy="880" rx="300" ry="170" fill="url(#wash-blush)"/>
      <ellipse cx="130" cy="730" rx="230" ry="180" fill="url(#wash-sand)"/>
      <ellipse cx="730" cy="640" rx="200" ry="150" fill="url(#wash-slate)"/>
      <ellipse cx="210" cy="880" rx="200" ry="120" fill="url(#wash-slate)"/>
      <ellipse cx="230" cy="50" rx="140" ry="60" fill="url(#wash-slate)"/>
      <ellipse cx="420" cy="700" rx="300" ry="150" fill="url(#wash-leaf)"/>
      <ellipse cx="800" cy="330" rx="70" ry="190" fill="url(#wash-gold)"/>
      <ellipse cx="600" cy="90" rx="120" ry="90" fill="url(#wash-white)"/>
      <ellipse cx="70" cy="300" rx="90" ry="110" fill="url(#wash-white)"/>
      <ellipse cx="590" cy="930" rx="130" ry="60" fill="url(#wash-white)"/>
    </svg>

    <h1 class="cover__title"><span>Lantern</span><span>Stones</span></h1>
    <p class="cover__subtitle">A Book of Gratitude and Inspiration</p>
    <p class="cover__author">Carl Wendover</p>
  </main>
</body>
</html>
```